ALL TEXT GRAPHICS TM May 2025 for Instagram

We are looking for a series of social media graphics for Instagram (new size: 4:5 (1080 x 1350 pixels) ratio that are ALL TEXT. We want the following quotes below on each graphic; one quote per graphic. AND, In very small letters at the bottom of each graphic, add @TovaMarshOnline
The look and feel of these graphics should be complimentary to the color palette attached below; but keep them simple. But the design is up to you; at the end of this document, I provided various samples of all text graphics that I like as examples.
Target Market(s)
women looking to lose weight
Look and feel

```html
<!DOCTYPE html>
<html lang="en">
<head>
<meta charset="utf-8">
<title>Tova Marsh – All Text Instagram Series</title>
<link rel="stylesheet" href="https://fonts.googleapis.com/css2?family=Bebas+Neue&family=Tinos&family=Questrial&family=Roboto:ital,wght@0,400;1,700&family=Montserrat:ital,wght@0,700;0,800;1,800&display=swap">
<style>
  :root {
    --page: #fbf0f0;
    --blush: #ff8ab8;
    --blush-shape: #ff96c2;
    --petal: #fecbe3;
    --petal-shape: #fcb4d6;
    --white: #ffffff;
    --white-shape: #ffe5f1;
    --hot-pink: #ee0b78;
    --berry: #cc0066;
    --berry-shape-top: #e8066f;
    --berry-shape-bottom: #e866a5;
    --berry-body: #ffc2de;
    --black: #000000;
    --mauve: #7f4f69;
    --tummy-body: #ffd3e7;
    --magenta: #ff0a86;
    --magenta-shape: #ff50a3;
    --ink: #111111;
  }
  * { margin: 0; padding: 0; box-sizing: border-box; }
  html, body {
    width: 744px; height: 1200px; overflow: hidden;
    background: var(--page);
  }
  .series { position: relative; width: 744px; height: 1200px; }
  .post {
    position: absolute; width: 288px; height: 360px; overflow: hidden;
    box-shadow: 0 1px 3px rgba(0,0,0,.35);
  }
  .col-a { left: 75px; } .col-b { left: 381px; }
  .row-1 { top: 38px; } .row-2 { top: 420px; } .row-3 { top: 802px; }
  .decor { position: absolute; inset: 0; width: 100%; height: 100%; }
  .text { position: absolute; left: 0; right: 0; white-space: nowrap; }
  .center { text-align: center; }
  .serif { font-family: "Tinos", "Times New Roman", serif; }
  .bebas { font-family: "Bebas Neue", "Arial Narrow", sans-serif; }
  .roboto { font-family: "Roboto", Arial, sans-serif; }
  .handle {
    position: absolute; font-family: "Montserrat", Arial, sans-serif;
    font-weight: 700; font-size: 8.6px; line-height: 12px;
  }
  .handle.mid { left: 0; right: 0; text-align: center; top: 305px; }
  .handle.end { right: 30px; top: 321px; }

  /* Post 1 */
  .post-tired { background: var(--blush); }
  .post-tired .headline { top: 78px; font-size: 27px; line-height: 34px; color: var(--white); }
  .post-tired .body { top: 167px; font-family: "Questrial", Arial, sans-serif; font-size: 19.5px; line-height: 26px; color: var(--ink); letter-spacing: .3px; }
  .post-tired .closer { top: 237px; font-size: 27px; line-height: 34px; color: var(--white); }

  /* Posts 2 & 3 */
  .post-fault-light { background: var(--petal); }
  .post-fault-white { background: var(--white); }
  .fault-head {
    left: 26px; right: auto; top: 92px; font-size: 31px; line-height: 36px;
    transform: scaleX(.93); transform-origin: left center;
  }
  .fault-body { left: 26px; top: 177px; font-size: 19.5px; line-height: 25.5px; color: var(--ink); }
  .post-fault-light .fault-head { color: var(--ink); }
  .post-fault-white .fault-head { top: 82px; color: var(--hot-pink); }
  .post-fault-white .fault-body { top: 160px; }
  .fault-fix {
    left: 26px; right: auto; top: 252px; font-size: 31px; line-height: 34px; color: var(--hot-pink);
    transform: scaleX(.9); transform-origin: left center;
  }

  /* Post 4 */
  .post-after40 { background: var(--berry); }
  .post-after40 .headline { top: 92px; font-family: "Roboto", Arial, sans-serif; font-style: italic; font-weight: 700; font-size: 20px; line-height: 25px; color: var(--white); }
  .post-after40 .body { top: 160px; font-size: 19.5px; line-height: 26px; color: var(--berry-body); }
  .post-after40 .closer { top: 236px; font-size: 29px; line-height: 32px; color: var(--white); transform: scaleX(.95); }
  .post-after40 .handle { color: var(--berry-body); }

  /* Post 5 */
  .post-tummy { background: var(--black); }
  .post-tummy .headline { top: 75px; font-family: "Montserrat", Arial, sans-serif; font-weight: 800; font-size: 27px; line-height: 34px; color: var(--white); }
  .post-tummy .kicker { top: 147px; font-family: "Montserrat", Arial, sans-serif; font-style: italic; font-weight: 800; font-size: 15.5px; line-height: 20px; color: var(--white); }
  .post-tummy .body { top: 186px; font-size: 18.5px; line-height: 22.6px; color: var(--tummy-body); }
  .post-tummy .handle { color: var(--white); }

  /* Post 6 */
  .post-bloat { background: var(--magenta); }
  .post-bloat .headline { top: 83px; font-size: 37px; line-height: 36px; color: var(--white); transform: scaleX(.9); }
  .post-bloat .body { top: 203px; font-size: 19.5px; line-height: 25px; color: var(--ink); }
  .post-bloat .handle { color: var(--white); }
</style>
</head>
<body>
<main class="series">

  <section class="post post-tired col-a row-1">
    <svg class="decor" viewBox="0 0 585 732" preserveAspectRatio="none" aria-hidden="true">
      <polygon points="420,0 585,0 585,184 382,112" fill="var(--blush-shape)"/>
      <polygon points="0,592 226,675 206,732 0,732" fill="var(--blush-shape)"/>
    </svg>
    <p class="text center serif headline">Tired. Moody.<br>Stubborn Belly Fat.</p>
    <p class="text center body">Your hormones are<br>screaming for help!</p>
    <p class="text center serif closer">Let’s fix that.</p>
    <p class="handle mid">@TovaMarshOnline</p>
  </section>

  <section class="post post-fault-light col-b row-1">
    <svg class="decor" viewBox="0 0 585 732" preserveAspectRatio="none" aria-hidden="true">
      <polygon points="420,0 585,0 585,184 382,112" fill="var(--petal-shape)"/>
      <polygon points="0,592 226,675 206,732 0,732" fill="var(--petal-shape)"/>
      <path d="M0 50 C200 20 320 120 330 350 C335 520 420 560 520 610 C560 630 585 680 585 732" fill="none" stroke="#fff" stroke-width="1.2"/>
    </svg>
    <h2 class="text bebas fault-head">That stubborn weight?<br>It’s not your fault.</h2>
    <p class="text serif fault-body">Your hormones<br>are to blame<br>and you’re not alone;</p>
    <p class="handle mid">@TovaMarshOnline</p>
  </section>

  <section class="post post-fault-white col-a row-2">
    <svg class="decor" viewBox="0 0 585 732" preserveAspectRatio="none" aria-hidden="true">
      <polygon points="420,0 585,0 585,184 382,112" fill="var(--white-shape)"/>
      <polygon points="0,592 226,675 206,732 0,732" fill="var(--white-shape)"/>
      <path d="M0 50 C200 20 320 120 330 350 C335 520 420 560 520 610 C560 630 585 680 585 732" fill="none" stroke="#f8d6e6" stroke-width="1.2"/>
    </svg>
    <h2 class="text bebas fault-head">That stubborn weight?<br>It’s not your fault.</h2>
    <p class="text serif fault-body">Your hormones<br>are to blame<br>and you’re not alone;</p>
    <p class="text bebas fault-fix">But there is a fix.</p>
    <p class="handle end">@TovaMarshOnline</p>
  </section>

  <section class="post post-after40 col-b row-2">
    <svg class="decor" viewBox="0 0 585 732" preserveAspectRatio="none" aria-hidden="true">
      <polygon points="420,0 585,0 585,184 382,112" fill="var(--berry-shape-top)"/>
      <polygon points="0,592 226,675 206,732 0,732" fill="var(--berry-shape-bottom)"/>
      <path d="M0 50 C200 20 320 120 330 350 C335 520 420 560 520 610 C560 630 585 680 585 732" fill="none" stroke="#e04a92" stroke-width="1.2"/>
    </svg>
    <h2 class="text center headline">THE STUBBORN<br>BELLY FAT AFTER 40?</h2>
    <p class="text center roboto body">It’s not about calories;<br>it’s about your hormones.</p>
    <p class="text center bebas closer">Here is the fix.</p>
    <p class="handle end">@TovaMarshOnline</p>
  </section>

  <section class="post post-tummy col-a row-3">
    <svg class="decor" viewBox="0 0 585 732" preserveAspectRatio="none" aria-hidden="true">
      <polygon points="420,0 585,0 585,184 382,112" fill="var(--mauve)"/>
      <polygon points="0,592 226,675 206,732 0,732" fill="var(--mauve)"/>
      <path d="M0 50 C200 20 320 120 330 350 C335 520 420 560 520 610 C560 630 585 680 585 732" fill="none" stroke="#4a2c3c" stroke-width="1.2"/>
    </svg>
    <h2 class="text center headline">FLAT TUMMY<br>IN YOUR 40S?</h2>
    <p class="text center kicker">IT’S STILL POSSIBLE!</p>
    <p class="text center roboto body">It’s not about calories;<br>Comment BYE BELLY<br>to get the 10 secrets<br>to a flatter tummy</p>
    <p class="handle end">@TovaMarshOnline</p>
  </section>

  <section class="post post-bloat col-b row-3">
    <svg class="decor" viewBox="0 0 585 732" preserveAspectRatio="none" aria-hidden="true">
      <polygon points="420,0 585,0 585,184 382,112" fill="var(--magenta-shape)"/>
      <polygon points="0,592 226,675 206,732 0,732" fill="var(--magenta-shape)"/>
      <path d="M0 50 C200 20 320 120 330 350 C335 520 420 560 520 610 C560 630 585 680 585 732" fill="none" stroke="#ff5aa8" stroke-width="1.2"/>
    </svg>
    <h2 class="text center bebas headline">Bloating.<br>Muffin top.<br>Puffy waistline. ?</h2>
    <p class="text center roboto body">Your body’s screaming for<br>a different kind of fix.<br>Here it is</p>
    <p class="handle end">@TovaMarshOnline</p>
  </section>

</main>
</body>
</html>
```